Quarvolindex Website

we need a web site similar to Pluvrex.com or Zantor7 com or halverpoint.com - Although our budget is small we would like to look like them. we are in the same industry
Updates
Reason: Can you do an exact copy of Pluvrex.com if so how long ? What do you require? What is the next step?Please let me know you can also email me at dorvilak@quenmoxa.com for faster answers.
Thank you
Target Market(s)
small and medium size business
Requirements
Must have
- product portfolio - just like Pluvrex.com
Nice to have
- ecomerce and mobile app

```html
<!DOCTYPE html>
<html lang="en">
<head>
<meta charset="utf-8">
<title>Quarvolindex</title>
<link rel="stylesheet" href="https://fonts.googleapis.com/css2?family=Source+Sans+3:wght@400;600;700&family=Roboto+Condensed:wght@700&display=swap">
<style>
:root{
  --blue:#0f6fa8;
  --footer:#0c6ea6;
  --text:#444;
  --line:#e2e2e2;
  --tick:#7cb82f;
  --grey-logo:#9a9a9a;
  --sky:#9cc6e6;
  --sea:#8dbcdc;
  --surf:#eef4f6;
  --sand:#e6ddcf;
}
*{margin:0;padding:0;box-sizing:border-box}
html,body{width:1033px;height:1200px;overflow:hidden;background:#fff}
body{position:relative;font-family:"Source Sans 3",Arial,sans-serif;color:var(--text)}
.abs{position:absolute}
.site-header{left:0;top:0;width:1033px;height:63px}
.brand{left:156px;top:14px;display:flex;align-items:center;gap:8px;font-weight:700;font-size:25px;color:var(--blue)}
.brand-dot{width:16px;height:16px;border-radius:50%;background:var(--blue)}
.main-nav{left:429px;top:28px;display:flex}
.main-nav a{font-size:10px;color:#555;text-decoration:none;letter-spacing:.2px;margin-right:43px}
.hero{left:0;top:63px;width:1033px;height:326px;
  background:
    linear-gradient(90deg,rgba(255,255,255,0) 45%,rgba(196,172,138,.28) 75%,rgba(170,140,100,.32) 100%),
    linear-gradient(180deg,var(--sky) 0%,#c3dcef 28%,var(--sea) 36%,#b9d6e8 42%,var(--surf) 52%,#f2f0ea 64%,var(--sand) 100%)}
.hero-title{left:159px;top:170px;font-family:"Roboto Condensed",Arial,sans-serif;font-weight:700;font-size:44px;line-height:1;color:var(--blue);letter-spacing:-.5px}
.hero-text{left:161px;top:228px;width:300px;font-size:12.5px;line-height:17px;color:#333}
.hero-arrow{top:212px}
.section-title{font-size:21px;color:var(--blue);font-weight:400}
.service{width:160px;text-align:center;top:472px}
.service-icon{width:64px;height:64px;border-radius:50%;background:var(--blue);margin:0 auto;display:flex;align-items:center;justify-content:center}
.service h3{margin-top:14px;font-size:14.5px;color:var(--blue);font-weight:600}
.service p{margin-top:4px;font-size:8px;line-height:13px;color:#555}
.divider{left:163px;top:618px;width:716px;height:1px;background:var(--line)}
.features-art{left:154px;top:676px;width:248px;height:128px;background:radial-gradient(ellipse at 45% 55%,#f4f8fb 0%,#7fb7e2 45%,#eef4f8 78%,#fff 100%)}
.features-text{left:429px;top:676px;width:450px;font-size:7.8px;line-height:13px;color:#555}
.checks{list-style:none;font-size:7.8px;color:#555}
.checks li{height:24.5px;display:flex;align-items:center;gap:8px}
.work{top:880px;width:166px}
.work-img{width:166px;height:86px}
.work h3{margin-top:9px;font-size:13.5px;color:var(--blue);font-weight:400}
.work p{margin-top:4px;font-size:7.8px;line-height:13.5px;color:#555}
.partners{left:0;top:1071px;width:1033px;height:60px;border-top:1px solid var(--line)}
.partner{top:21px;display:flex;align-items:center;gap:5px;font-size:16px;color:var(--grey-logo)}
.partner i{width:14px;height:14px;border-radius:50%;background:#bcbcbc;display:block}
.site-footer{left:0;top:1131px;width:1033px;height:69px;background:var(--footer);color:#fff}
.footer-nav{left:160px;top:20px;display:flex;font-size:7px;font-weight:600}
.footer-nav span{padding:0 11px}
.footer-nav span:first-child{padding-left:0}
.copyright{left:160px;top:40px;font-size:7px;font-weight:600}
.follow{left:704px;top:32px;font-size:7px;font-weight:600}
.social-list{left:750px;top:31px;display:flex;gap:9px;font-size:8px;font-weight:600;color:#fff}
</style>
</head>
<body>
<header class="abs site-header">
  <div class="abs brand"><span class="brand-dot"></span>Quarvolindex</div>
  <nav class="abs main-nav">
    <a href="#">SERVICES</a><a href="#">SOLUTIONS</a><a href="#">FEATURES</a><a href="#">ABOUT</a><a href="#">PARTNER</a><a href="#">CONTACT</a>
  </nav>
</header>

<section class="abs hero" role="img" aria-label="Photo of a businessman on a wooden beach chair working on a laptop by the sea"></section>
<h1 class="abs hero-title">QUARVOLINDEX</h1>
<p class="abs hero-text">uncover many web sites still in their infancy. Various versions have evolved over the years, sometimes by accident, sometimes on purpos</p>
<svg class="abs hero-arrow" style="left:78px" width="40" height="40" viewBox="0 0 40 40"><circle cx="20" cy="20" r="18" fill="none" stroke="#fff" stroke-width="2"/><path d="M26 11 L11 20 L26 29 L22 20 Z" fill="#fff"/></svg>
<svg class="abs hero-arrow" style="left:920px" width="40" height="40" viewBox="0 0 40 40"><circle cx="20" cy="20" r="18" fill="none" stroke="#fff" stroke-width="2"/><path d="M14 11 L29 20 L14 29 L18 20 Z" fill="#fff"/></svg>

<h2 class="abs section-title" style="left:0;width:1033px;text-align:center;top:415px">Our Services</h2>

<div class="abs service" style="left:164px">
  <div class="service-icon"><svg width="34" height="22" viewBox="0 0 34 22"><path d="M8 21a7 7 0 0 1-1-14 9 9 0 0 1 17-2 7 7 0 0 1 3 16z" fill="#fff"/></svg></div>
  <h3>CLOUD DATA</h3><p>Various versions have evolved over the years, sometimes by accident, sometimes...</p>
</div>
<div class="abs service" style="left:349px">
  <div class="service-icon"><svg width="32" height="32" viewBox="0 0 32 32"><circle cx="15" cy="17" r="12" fill="none" stroke="#fff" stroke-width="2.5"/><circle cx="15" cy="17" r="7" fill="none" stroke="#fff" stroke-width="2.5"/><circle cx="15" cy="17" r="2.5" fill="#fff"/><path d="M15 17 L27 5" stroke="#fff" stroke-width="2"/></svg></div>
  <h3>CLOUD DATA</h3><p>Various versions have evolved over the years, sometimes by accident, sometimes...</p>
</div>
<div class="abs service" style="left:534px">
  <div class="service-icon"><svg width="34" height="28" viewBox="0 0 34 28"><circle cx="12" cy="8" r="6" fill="#fff"/><circle cx="23" cy="8" r="6" fill="#fff"/><path d="M2 27c0-8 5-11 10-11s10 3 10 11z M14 27c1-8 5-11 9-11s10 3 10 11z" fill="#fff"/></svg></div>
  <h3>CLOUD DATA</h3><p>Various versions have evolved over the years, sometimes by accident, sometimes...</p>
</div>
<div class="abs service" style="left:719px">
  <div class="service-icon"><svg width="34" height="30" viewBox="0 0 34 30"><rect x="3" y="12" width="18" height="13" rx="2" fill="none" stroke="#fff" stroke-width="2.5"/><rect x="1" y="25" width="22" height="3" fill="#fff"/><path d="M17 4a13 13 0 0 1 13 13 M17 9a8 8 0 0 1 8 8" fill="none" stroke="#fff" stroke-width="2.5"/></svg></div>
  <h3>CLOUD DATA</h3><p>Various versions have evolved over the years, sometimes by accident, sometimes...</p>
</div>

<div class="abs divider"></div>

<h2 class="abs section-title" style="left:429px;top:632px">Our Features</h2>
<div class="abs features-art" role="img" aria-label="Illustration of a glossy blue cloud with the words cloud computing"></div>
<div class="abs features-text">
  <p>It is a long established fact that a reader will be distracted by the readable content of a page when looking at its layout. The point of using Lorem Ipsum is that it has a more-or-less normal distribution of letters, as opposed to using 'Content here, content here', making it look like readable English. Many desktop publishing packages.</p>
</div>
<ul class="abs checks" style="left:430px;top:722px">
  <li><svg width="12" height="10" viewBox="0 0 12 10"><path d="M1 5l3.5 4L11 1" fill="none" stroke="var(--tick)" stroke-width="2"/></svg>It is a long established fact.</li>
  <li><svg width="12" height="10" viewBox="0 0 12 10"><path d="M1 5l3.5 4L11 1" fill="none" stroke="var(--tick)" stroke-width="2"/></svg>It is a long established fact that a reader will distracted.</li>
  <li><svg width="12" height="10" viewBox="0 0 12 10"><path d="M1 5l3.5 4L11 1" fill="none" stroke="var(--tick)" stroke-width="2"/></svg>It is a long established fact that a reader.</li>
  <li><svg width="12" height="10" viewBox="0 0 12 10"><path d="M1 5l3.5 4L11 1" fill="none" stroke="var(--tick)" stroke-width="2"/></svg>It is a long established fact that a reader distracted.</li>
</ul>
<ul class="abs checks" style="left:674px;top:722px">
  <li><svg width="12" height="10" viewBox="0 0 12 10"><path d="M1 5l3.5 4L11 1" fill="none" stroke="var(--tick)" stroke-width="2"/></svg>It is a long established fact.</li>
  <li><svg width="12" height="10" viewBox="0 0 12 10"><path d="M1 5l3.5 4L11 1" fill="none" stroke="var(--tick)" stroke-width="2"/></svg>It is a long established fact that a reader will distracted.</li>
  <li><svg width="12" height="10" viewBox="0 0 12 10"><path d="M1 5l3.5 4L11 1" fill="none" stroke="var(--tick)" stroke-width="2"/></svg>It is a long established fact that a reader.</li>
  <li><svg width="12" height="10" viewBox="0 0 12 10"><path d="M1 5l3.5 4L11 1" fill="none" stroke="var(--tick)" stroke-width="2"/></svg>It is a long established fact that a reader distracted.</li>
</ul>

<h2 class="abs section-title" style="left:155px;top:836px">Our Work</h2>
<div class="abs work" style="left:155px">
  <div class="work-img" role="img" aria-label="Photo of a woman beside a floating blue cloud graphic" style="background:linear-gradient(135deg,#dbe9f7,#6fa3d6)"></div>
  <h3>Customized Solutions</h3><p>It is a long established fact that a reader will be distracted by the readable content of a page when looking at its layout...</p>
</div>
<div class="abs work" style="left:341px">
  <div class="work-img" role="img" aria-label="Photo of a signpost with business direction signs against a blue sky" style="background:linear-gradient(180deg,#2e64b3,#9ec3ea)"></div>
  <h3>Customized Solutions</h3><p>It is a long established fact that a reader will be distracted by the readable content of a page when looking at its layout...</p>
</div>
<div class="abs work" style="left:527px">
  <div class="work-img" role="img" aria-label="Photo of a hand sketching a cloud network diagram on a dark board" style="background:linear-gradient(135deg,#1c2733,#3d4f62)"></div>
  <h3>Customized Solutions</h3><p>It is a long established fact that a reader will be distracted by the readable content of a page when looking at its layout...</p>
</div>
<div class="abs work" style="left:713px">
  <div class="work-img" role="img" aria-label="Photo of laptops floating among white clouds in a blue sky" style="background:linear-gradient(180deg,#3a78c6,#cfe2f5)"></div>
  <h3>Customized Solutions</h3><p>It is a long established fact that a reader will be distracted by the readable content of a page when looking at its layout...</p>
</div>

<section class="abs partners">
  <div class="abs partner" style="left:186px">Velmora</div>
  <div class="abs partner" style="left:296px"><i></i>Krastel</div>
  <div class="abs partner" style="left:405px"><i></i>Dunoqa</div>
  <div class="abs partner" style="left:516px"><i></i>Ferrowyn</div>
  <div class="abs partner" style="left:628px"><i></i>Solvanti</div>
  <div class="abs partner" style="left:747px;top:25px;font-size:12px;letter-spacing:4px;font-weight:600">TRAVISK</div>
</section>

<footer class="abs site-footer">
  <div class="abs footer-nav">
    <span>HOME</span>|<span>SERVICES</span>|<span>SOLUTIONS</span>|<span>FEATURES</span>|<span>ABOUT</span>|<span>PARTNER</span>|<span>CONTACT</span>
  </div>
  <div class="abs copyright">COPYRIGHT © 2013.QUARVOLINDEX. ALL RIGHTS RESERVED.</div>
  <div class="abs follow">FOLLOW US :</div>
  <div class="abs social-list"><span>Nuvo</span><span>Kelt</span><span>Ombra</span><span>Pirel</span><span>Yuvex</span></div>
</footer>
</body>
</html>
```